Boutique Wealth management firm needs a new business card design

I want to update my business card design to be more consistent with the look and feel of my website (www.brisvane-wealth.com). I would like to incorporate an ivory parchment background and am open to switching from the current "portrait" layout to a more traditional "landscape" orientation. The final design should convey stability and exclusivity and I want something in PDF format that is ready to send to the printer

Thank you all for taking the time to submit your designs for my project. I've made my decision and picked the design I like best. Thanks again!

```html
<!DOCTYPE html>
<html lang="en">
<head>
<meta charset="utf-8">
<title>Brisvane Wealth Advisory – Business Card</title>
<link rel="stylesheet" href="https://fonts.googleapis.com/css2?family=Exo+2:wght@500&family=Open+Sans:wght@400&display=swap">
<style>
  :root {
    --parchment: #f1e9d2;
    --parchment-edge: #e6dab9;
    --card-ivory: #fdfaf2;
    --charcoal: #3b3b3d;
    --charcoal-dark: #2c2c2e;
    --maroon: #6a2740;
    --maroon-line: #8c5a6d;
    --ink: #2e2e30;
    --silver: #c9c9cc;
    --on-maroon: #ffffff;
  }
  * { box-sizing: border-box; margin: 0; padding: 0; }
  html, body {
    width: 1200px;
    height: 939px;
    overflow: hidden;
    background: var(--parchment);
  }
  .canvas {
    position: relative;
    width: 1200px;
    height: 939px;
    background: radial-gradient(ellipse at center, var(--parchment) 55%, var(--parchment-edge) 100%);
  }
  .card {
    position: absolute;
    left: 110px;
    top: 190px;
    width: 980px;
    height: 560px;
    background: var(--charcoal);
    box-shadow: 0 18px 40px rgba(60,45,20,0.25);
    overflow: hidden;
  }
  .card-head {
    position: absolute;
    left: 0; top: 0;
    width: 100%;
    height: 250px;
    background: var(--card-ivory);
  }
  .person {
    position: absolute;
    left: 70px;
    top: 98px;
    font-family: "Exo 2", sans-serif;
    font-weight: 500;
    color: var(--ink);
  }
  .person-name { font-size: 40px; letter-spacing: 1px; line-height: 1.1; }
  .person-role { font-size: 30px; letter-spacing: 1px; margin-top: 10px; margin-left: 8px; }
  .brand {
    position: absolute;
    right: 100px;
    top: 88px;
    display: flex;
    align-items: center;
    gap: 12px;
    font-family: "Exo 2", sans-serif;
    font-weight: 500;
    font-size: 28px;
    letter-spacing: 0.5px;
    color: var(--maroon);
  }
  .brand-mark {
    width: 18px;
    height: 18px;
    background: var(--maroon);
  }
  .contact-panel {
    position: absolute;
    left: 60px;
    right: 28px;
    top: 250px;
    height: 250px;
    display: flex;
    background: var(--maroon);
    border-right: 3px solid var(--silver);
    border-bottom: 3px solid var(--silver);
  }
  .contact-cell {
    flex: 1;
    display: flex;
    flex-direction: column;
    align-items: center;
    justify-content: space-between;
    padding: 50px 10px 40px;
    border-left: 1px solid var(--maroon-line);
    font-family: "Open Sans", sans-serif;
    font-size: 21px;
    color: var(--on-maroon);
  }
  .contact-cell:first-child { border-left: none; }
  .contact-icon { width: 34px; height: 34px; }
  .card-base {
    position: absolute;
    left: 0; bottom: 0;
    width: 100%;
    height: 60px;
    background: var(--charcoal-dark);
  }
</style>
</head>
<body>
<main class="canvas">
  <article class="card">
    <header class="card-head">
      <div class="person">
        <p class="person-name">Johnathan Doe</p>
        <p class="person-role">Manager</p>
      </div>
      <div class="brand">
        <span class="brand-mark" aria-hidden="true"></span>
        <span class="brand-name">Brisvane Wealth Advisory</span>
      </div>
    </header>

    <section class="contact-panel">
      <div class="contact-cell">
        <svg class="contact-icon" viewBox="0 0 34 34" aria-hidden="true">
          <rect x="5" y="9" width="24" height="16" fill="#fff"/>
          <path d="M5 9 L17 19 L29 9" fill="none" stroke="#6a2740" stroke-width="2"/>
        </svg>
        <span>info@youremail.com</span>
      </div>
      <div class="contact-cell">
        <svg class="contact-icon" viewBox="0 0 34 34" aria-hidden="true">
          <path d="M10 4 L14 4 L16 11 L13 13 C14 18 16 21 21 23 L23 20 L30 22 L30 26 C30 28 28 30 26 30 C15 29 5 19 4 8 C4 6 6 4 8 4 Z" fill="#fff"/>
        </svg>
        <span>+2 (0111) 32-333-22</span>
      </div>
      <div class="contact-cell">
        <svg class="contact-icon" viewBox="0 0 34 34" aria-hidden="true">
          <g fill="none" stroke="#fff" stroke-width="2">
            <circle cx="17" cy="17" r="13"/>
            <ellipse cx="17" cy="17" rx="6" ry="13"/>
            <line x1="4" y1="17" x2="30" y2="17"/>
            <line x1="17" y1="4" x2="17" y2="30"/>
            <path d="M7 10 H27 M7 24 H27"/>
          </g>
        </svg>
        <span>www.website.com</span>
      </div>
    </section>

    <div class="card-base"></div>
  </article>
</main>
</body>
</html>
```